New website design and logo for BrazeKit.com to help ignite the website sales.

Hi designers,

Brazekit is a new welding brand that is selling welding equipement.

Currently I have around 5 to 10 products. The issue is that the site itself does not do that much of sales. So I have to do something about the seo etc. but that is out of scope for the design.

What is in scope is to comeup with a new logo and website look and feel that is in line with the customers.

men, non professionals, garage, home improvements, perhaps sme ( small mediul entreprice business that want to start in the welding industry.

Products are midrange prices and quality. The look and feel must breath cool stuff, sexy ( women in working cloths carrying welding gloves, other protection gear and weldels)

The wedsite is build in wordpress with the Lumo theme. I am an IT guy myself withhout any creativity in me :( so if you can help me with that that would be great.

Please have a quick look at brazekit.com

Best regards,
Joost

Target Market(s)

non professional welders that do metal work in there garage

Coding

Coded - Design and coding required

Number of Pages Required

3 page

Font styles to use
Sans Serif

Colors
0355a3
ffc214

Requirements
Must have
• I would like to see a new homepage and product page design together with a new logo.
Nice to have
• shop design

```html
<!DOCTYPE html>
<html lang="en">
<head>
<meta charset="utf-8">
<title>Brazekit – Welding Equipment</title>
<link href="https://fonts.googleapis.com/css2?family=Audiowide&family=Oswald:wght@500&family=Roboto:wght@400;500;700&display=swap" rel="stylesheet">
<style>
:root{
  --blue:#0355a3;
  --blue-bright:#0b6fce;
  --blue-dark:#02407d;
  --yellow:#ffc214;
  --orange:#f39c12;
  --ink:#1d1d1d;
  --text:#444;
  --muted:#9a9a9a;
  --light:#f4f4f4;
  --black:#121212;
}
*{margin:0;padding:0;box-sizing:border-box}
html,body{width:1200px;height:4605px;overflow:hidden}
body{font-family:Roboto,Arial,sans-serif;color:var(--text);background:#fff;position:relative}
.abs{position:absolute}
a{color:inherit;text-decoration:none}
.heading{font-family:Audiowide,Arial,sans-serif;text-transform:uppercase;letter-spacing:2px;color:var(--ink);font-weight:400}
.heading span{color:var(--blue)}
.center{text-align:center;left:0;width:1200px}
.lede{font-size:14px;line-height:23px;color:#333}

/* top bar */
.topbar{top:0;left:0;width:1200px;height:40px;background:var(--blue);color:#fff;font-size:14px;font-weight:500}
.topbar .ship{left:100px;top:11px}
.topbar .help{right:110px;top:11px}

/* header */
.header{top:40px;left:0;width:1200px;height:103px;background:#fff}
.logo{left:100px;top:22px;display:flex;align-items:center;gap:10px}
.logo .dot{width:22px;height:22px;border-radius:50%;background:var(--yellow)}
.logo b{font-family:Audiowide,sans-serif;font-weight:400;font-size:31px;color:var(--blue);letter-spacing:1px}
.search{left:378px;top:15px;width:444px;height:38px;border:1px solid #bbb;border-radius:19px;display:flex;align-items:center;font-size:12px;color:#555;overflow:hidden}
.search .cat{width:147px;padding-left:20px;border-right:1px solid #bbb;height:100%;display:flex;align-items:center;gap:8px}
.search .field{flex:1;padding-left:14px}
.search .btn{width:52px;height:100%;background:var(--blue);display:flex;align-items:center;justify-content:center}
.account{left:838px;top:17px;display:flex;gap:8px;font-size:13px;color:#222;line-height:15px}
.cart{left:1005px;top:17px;display:flex;gap:8px;font-size:13px;color:#222;line-height:15px}
.nav{top:73px;left:377px;display:flex;font-size:15px;font-weight:500;color:#111}
.nav li{list-style:none;display:flex;align-items:center}
.nav li+li::before{content:"|";margin:0 38px;color:#333}
.nav .active{color:var(--blue)}

/* hero */
.hero{top:143px;left:0;width:1200px;height:590px;
  background:
    radial-gradient(ellipse 160px 120px at 760px 470px,rgba(255,120,200,.55),transparent 70%),
    radial-gradient(ellipse 110px 80px at 860px 90px,rgba(70,130,230,.55),transparent 70%),
    radial-gradient(ellipse 260px 260px at 850px 230px,rgba(120,120,130,.55),transparent 75%),
    radial-gradient(ellipse 220px 280px at 560px 200px,rgba(140,135,130,.45),transparent 75%),
    linear-gradient(180deg,#3a3c40 0%,#4a4846 60%,#2b2b2d 100%)}
.hero h1{left:100px;top:190px;font-family:Oswald,sans-serif;font-weight:500;font-size:40px;line-height:52px;color:#fff;text-transform:uppercase}
.hero .buy{left:100px;top:377px;width:158px;height:44px;border-radius:22px;background:var(--yellow);color:#fff;font-weight:700;font-size:15px;display:flex;align-items:center;justify-content:center}
.hero .arrow{top:305px}
.dots{top:557px;left:562px;display:flex;gap:8px}
.dots i{width:11px;height:11px;border-radius:50%;border:1.5px solid #fff}
.dots i.on{background:#fff}

/* products */
.card{width:239px}
.card .ph{height:268px;background:#f3f3f3}
.card .meta{text-align:center;padding-top:12px;font-size:13px;line-height:22px}
.stars{color:var(--orange);letter-spacing:1px;font-size:12px}
.card .name{color:var(--blue)}
.card .price{color:#111}
.card .price s{color:#999;margin-right:4px}
.badge{top:8px;right:8px;width:42px;height:42px;border-radius:50%;background:var(--yellow);color:#222;font-size:11px;font-weight:700;line-height:11px;display:flex;flex-direction:column;align-items:center;justify-content:center}
.ph.machine-red{background:radial-gradient(ellipse 70px 110px at 50% 50%,#c9402f 0%,#8e2a20 45%,rgba(243,243,243,0) 80%),#f3f3f3}
.ph.helmet{background:radial-gradient(ellipse 85px 105px at 50% 50%,#2a2a2c 0%,#505054 40%,rgba(243,243,243,0) 80%),radial-gradient(ellipse 28px 30px at 42% 42%,#a86be0,transparent),#f3f3f3}
.ph.machine-blue{background:radial-gradient(ellipse 95px 100px at 50% 50%,#3a7fd6 0%,#b9c2cc 45%,rgba(243,243,243,0) 80%),#f3f3f3}
.ph.gloves-blue{background:radial-gradient(ellipse 60px 60px at 62% 35%,#2a45b8,transparent 90%),radial-gradient(ellipse 70px 60px at 40% 62%,#e8b521,transparent 90%),#f3f3f3}
.ph.triangle{background:linear-gradient(135deg,rgba(243,243,243,0) 8%,#2a2220 10%,#3a302c 48%,rgba(243,243,243,0) 52%),#f3f3f3}
.ph.gloves-black{background:radial-gradient(ellipse 80px 110px at 50% 50%,#2b2b28 0%,#4c4b40 45%,rgba(243,243,243,0) 80%),#f3f3f3}

/* about */
.about{top:1725px;left:0;width:1200px;height:349px;background:radial-gradient(ellipse 260px 200px at 160px 90px,rgba(120,170,230,.35),transparent 70%),linear-gradient(90deg,#0a3f7e 0%,#0355a3 45%,#0e5fb0 100%);color:#fff}
.about h2{left:160px;top:92px;font-size:32px;line-height:40px;color:#fff}
.about .more{left:159px;top:207px;width:218px;height:45px;border:1.5px solid #fff;display:flex;align-items:center;justify-content:center;font-size:14px;font-weight:500}
.about p{font-size:14.5px;line-height:26px}

/* benefits */
.benefits{top:2074px;left:0;width:1200px;height:635px;background:var(--light)}
.benefit{font-size:12px;line-height:17px;color:#333;width:240px}
.benefit b{display:block;font-size:15px;color:#111;font-weight:500;margin-bottom:4px}
.benefit.right{text-align:right}

/* blog */
.post{width:317px}
.post .ph{height:236px}
.post .box{position:absolute;left:15px;top:197px;width:287px;height:215px;background:#fff;border-radius:6px;box-shadow:0 2px 12px rgba(0,0,0,.08);padding:22px 18px}
.post .date{font-size:12px;color:#333;display:flex;align-items:center;gap:8px}
.post h3{font-size:16px;line-height:26px;font-weight:500;color:#111;margin-top:12px}
.post p{font-size:12.5px;line-height:22px;color:var(--muted);margin-top:8px}
.post .read{font-size:13px;font-weight:700;color:var(--orange);margin-top:12px;display:block}

/* faq */
.faq{top:3442px;left:0;width:1200px;height:501px;background:linear-gradient(90deg,#0355a3,#0b62b9 60%,#0355a3)}
.faq h2{color:#fff;font-size:32px}
.q{background:#fff;height:46px;display:flex;align-items:center;justify-content:space-between;padding:0 14px;font-size:13.5px;color:#111}
.q .sign{font-size:26px;font-weight:300;color:#333}
.qa{background:#fff;padding:0 14px}
.qa .q{padding:0;border-bottom:1px solid #eee}
.qa .ans{display:flex;gap:16px;padding:12px 0 14px;font-size:11.5px;line-height:20px;color:var(--muted)}

/* newsletter */
.news h2{font-size:19px;letter-spacing:2px}
.news .input{left:573px;top:4012px;width:557px;height:62px;border:1px solid #ddd;border-radius:31px;font-size:13px;color:#666;padding-left:28px;display:flex;align-items:center}
.news .sub{left:962px;top:4012px;width:168px;height:62px;border-radius:31px;background:var(--yellow);color:#fff;font-weight:700;font-size:15px;display:flex;align-items:center;justify-content:center}

/* features */
.features{top:4127px;left:0;width:1200px;height:93px;display:flex}
.feat{width:300px;height:100%;display:flex;align-items:center;gap:10px;padding-left:22px;color:#fff;font-size:12px;line-height:14px;white-space:nowrap}
.feat:first-child{padding-left:52px}
.feat b{display:block;font-size:14px;font-weight:500;text-transform:uppercase}
.feat.a{background:var(--blue)}
.feat.b{background:var(--blue-bright)}

/* footer */
.footer{top:4220px;left:0;width:1200px;height:385px;background:var(--black);color:#fff}
.fcol h4{font-size:16px;font-weight:500;text-transform:uppercase;margin-bottom:18px}
.fcol ul{list-style:none;font-size:13px;line-height:29px}
.fcol p{font-size:12.5px;line-height:23px}
.femail{width:250px;height:38px;border-radius:19px;background:#fff;color:#777;font-size:13px;padding-left:12px;display:flex;align-items:center;justify-content:space-between;padding-right:4px}
.social{display:flex;gap:12px}
.social i{width:42px;height:42px;border-radius:50%;border:1.5px solid #fff;display:block}
.pay{display:flex;gap:22px;font-size:13px;font-weight:700;color:#8c8c8c}
</style>
</head>
<body>

<div class="abs topbar">
  <div class="abs ship">&#9951; Free shipping from € 30.00</div>
  <div class="abs help">We're here to help! &nbsp;☏ Call +31(0)645217390</div>
</div>

<header class="abs header">
  <a class="abs logo" href="#"><span class="dot"></span><b>BRAZEKIT</b></a>
  <div class="abs search">
    <div class="cat">Select Category <svg width="9" height="6"><path d="M0 0h9L4.5 6z" fill="#333"/></svg></div>
    <div class="field">Select Here...</div>
    <div class="btn"><svg width="18" height="18" fill="none" stroke="#fff" stroke-width="2"><circle cx="8" cy="8" r="6"/><path d="M12.5 12.5L17 17"/></svg></div>
  </div>
  <div class="abs account">
    <svg width="30" height="30" fill="none" stroke="#222" stroke-width="1.8"><circle cx="15" cy="15" r="13"/><circle cx="15" cy="12" r="5"/><path d="M6 24c3-5 15-5 18 0"/></svg>
    <div>Welcome<br>Sign In / Register</div>
  </div>
  <div class="abs cart">
    <svg width="34" height="30" fill="none" stroke="#222" stroke-width="1.8"><path d="M1 3h5l4 17h18l4-12H8"/><circle cx="12" cy="26" r="2"/><circle cx="26" cy="26" r="2"/></svg>
    <div>My Cart<br>€ 00.00</div>
  </div>
  <ul class="abs nav">
    <li class="active">HOME</li><li>ABOUT US</li><li>GLOVES</li><li>MIG</li><li>BLOG</li><li>CONTACT US</li>
  </ul>
</header>

<section class="abs hero" role="img" aria-label="Two welders in protective helmets and jackets welding steel with sparks flying">
  <h1 class="abs">Simple welding of steel &amp;<br>aluminumget great results<br>with tools that work</h1>
  <a class="abs buy" href="#">BUY NOW</a>
  <svg class="abs arrow" style="left:48px" width="18" height="34" fill="none" stroke="#fff" stroke-width="2"><path d="M16 2L2 17l14 15"/></svg>
  <svg class="abs arrow" style="left:1112px" width="18" height="34" fill="none" stroke="#fff" stroke-width="2"><path d="M2 2l14 15L2 32"/></svg>
  <div class="abs dots"><i class="on"></i><i></i><i></i><i></i></div>
</section>

<h2 class="abs heading center" style="top:816px;font-size:34px">Our <span>Products</span></h2>
<p class="abs lede center" style="top:862px">Lorem ipsum dolor sit amet, consectetur adipiscing elit, sed do eiusmod tempor incididunt<br>ut labore et dolore magna aliqua. Quis ipsum suspendisse ultrices gravida.</p>

<div class="abs card" style="left:100px;top:948px"><div class="ph machine-red" role="img" aria-label="Red MIG welding machine"></div><div class="abs badge">10%<br>OFF</div><div class="meta"><div class="stars">★★★★★</div><div class="name">MIG-250P</div><div class="price"><s>€ 845.00</s>€ 795.00</div></div></div>
<div class="abs card" style="left:354px;top:948px"><div class="ph helmet" role="img" aria-label="Black welding helmet with purple visor, side view"></div><div class="meta"><div class="stars">★★★★★</div><div class="name">Welding helmet 180 degrees view</div><div class="price">€ 795.00</div></div></div>
<div class="abs card" style="left:608px;top:948px"><div class="ph machine-blue" role="img" aria-label="Blue and silver MIG welding machine"></div><div class="meta"><div class="stars">★★★★★</div><div class="name">MIG-2500</div><div class="price">€ 795.00</div></div></div>
<div class="abs card" style="left:862px;top:948px"><div class="ph helmet" role="img" aria-label="Black welding helmet with large purple visor"></div><div class="meta"><div class="stars">★★★★★</div><div class="name">Welding helmet large view</div><div class="price"><s>€ 845.00</s>€</div></div></div>

<div class="abs card" style="left:100px;top:1300px"><div class="ph gloves-blue" role="img" aria-label="Blue and yellow leather welding gloves"></div><div class="meta"><div class="stars">★★★★★</div><div class="name">Welding gloves Blue</div><div class="price">€22,40</div></div></div>
<div class="abs card" style="left:354px;top:1300px"><div class="ph triangle" role="img" aria-label="Black aluminium measuring triangle"></div><div class="abs badge">10%<br>OFF</div><div class="meta"><div class="stars">★★★★★</div><div class="name">Large measuring triangle | 12 inches</div><div class="price"><s>€ 845.00</s>€ 795.00</div></div></div>
<div class="abs card" style="left:608px;top:1300px"><div class="ph gloves-black" role="img" aria-label="Black leather welding gloves"></div><div class="meta"><div class="stars">★★★★★</div><div class="name">Welding gloves Black</div><div class="price">€22,40</div></div></div>
<div class="abs card" style="left:862px;top:1300px"><div class="ph triangle" role="img" aria-label="Small black measuring triangle"></div><div class="meta"><div class="stars">★★★★★</div><div class="name">Kleine meetdriehoek | 7 inch</div><div class="price"><s>€ 845.00</s>€ 795.00</div></div></div>

<section class="abs about" role="img" aria-label="Blue-toned backdrop of a welder at work">
  <h2 class="abs heading" style="color:#fff">About<br>Brazekit</h2>
  <a class="abs more" href="#">LEARN MORE ABOUT US</a>
  <div class="abs" style="left:474px;top:88px;width:560px">
    <p>Lorem ipsum dolor sit amet, consectetur adipiscd do eiusmod tempor incidunt ut laborgna aliqua. Quis ipsum suspendisse ultrices gravida.</p>
    <p style="margin-top:10px">Lorem ipsum dolor sit amet, consectetur adipiscd do eiusmod temnt ut laborgna aliqua. Quis ipsum suspendisse ultrices gravida.Lorem ipsur sit amet, consectetur adipiscd do eiusmod tempor incidunt ut laborgna aliqua.Lorem ipsum dolor sit amet, consectetur adipiscd do eiusmod temnt ut laborgna aliqua.</p>
  </div>
</section>

<section class="abs benefits">
  <h2 class="abs heading center" style="top:72px;font-size:34px">Brazekit <span>Benefits</span></h2>
  <svg class="abs" style="left:0;top:0" width="1200" height="635" fill="none" stroke="var(--blue)" stroke-width="2">
    <circle cx="598" cy="341" r="152"/>
    <path d="M506 211L420 182M660 200L742 170M443 338H347M747 338H844M531 472L448 511M660 472L745 510"/>
    <g fill="#fff">
      <circle cx="506" cy="211" r="7"/><circle cx="660" cy="200" r="7"/><circle cx="443" cy="338" r="7"/><circle cx="747" cy="338" r="7"/><circle cx="531" cy="472" r="7"/><circle cx="660" cy="472" r="7"/>
      <circle cx="377" cy="182" r="44"/><circle cx="302" cy="336" r="44"/><circle cx="404" cy="511" r="44"/>
      <circle cx="787" cy="170" r="44"/><circle cx="889" cy="338" r="44"/><circle cx="789" cy="510" r="44"/>
    </g>
    <g stroke-width="1.6">
      <rect x="362" y="166" width="28" height="32" rx="2"/><path d="M367 176h18M367 184h18M367 192h10"/>
      <circle cx="302" cy="326" r="10"/><path d="M284 350h20l12-8"/>
      <rect x="390" y="496" width="26" height="32" rx="2"/><circle cx="408" cy="516" r="7"/>
      <path d="M770 172l10-8 10 8 10-8 6 6-16 14-16-12z"/>
      <rect x="877" y="324" width="24" height="30" rx="2"/><path d="M881 332h16M881 340h16M881 348h16"/>
      <circle cx="789" cy="510" r="16"/><rect x="782" y="508" width="14" height="11"/><path d="M785 508v-4a4 4 0 018 0v4"/>
    </g>
  </svg>
  <div class="abs" style="left:478px;top:319px;width:240px;text-align:center;font-family:Audiowide,sans-serif;font-size:30px;color:var(--blue)">BRAZEKIT</div>
  <div class="abs benefit right" style="left:73px;top:152px"><b>The standard Lorem</b>Lorem ipsum dolor sit amet,<br>consectetur adipiscing elit, sed do</div>
  <div class="abs benefit right" style="left:1px;top:312px"><b>The standard Lorem</b>Lorem ipsum dolor sit amet,<br>consectetur adipiscing elit, sed do</div>
  <div class="abs benefit right" style="left:103px;top:488px"><b>The standard Lorem</b>Lorem ipsum dolor sit amet,<br>consectetur adipiscing elit, sed do</div>
  <div class="abs benefit" style="left:842px;top:136px"><b>The standard Lorem</b>Lorem ipsum dolor sit amet,<br>consectetur adipiscing elit, sed do</div>
  <div class="abs benefit" style="left:944px;top:302px"><b>The standard Lorem</b>Lorem ipsum dolor sit amet,<br>consectetur adipiscing elit, sed do</div>
  <div class="abs benefit" style="left:848px;top:480px"><b>The standard Lorem</b>Lorem ipsum dolor sit amet,<br>consectetur adipiscing elit, sed do</div>
</section>

<h2 class="abs heading center" style="top:2794px;font-size:34px">Latest <span>Blog</span></h2>
<p class="abs lede center" style="top:2840px">Lorem ipsum dolor sit amet, consectetur adipiscing elit, sed do eiusmod tempor incididunt<br>ut labore et dolore magna aliqua. Quis ipsum suspendisse ultrices gravida.</p>

<article class="abs post" style="left:100px;top:2928px">
  <div class="ph" role="img" aria-label="Welder in helmet working under blue arc light" style="background:radial-gradient(ellipse 90px 70px at 35% 40%,#cfe2ff,rgba(80,130,220,.6) 40%,transparent 75%),linear-gradient(135deg,#12204a,#2e55a0 50%,#141a33)"></div>
  <div class="box"><div class="date"><svg width="16" height="16" fill="none" stroke="var(--blue)" stroke-width="1.4"><rect x="1" y="3" width="14" height="12"/><path d="M1 7h14M5 1v4M11 1v4"/></svg>November 14, 2021</div><h3>Lorem ipsum doloet, consectetur adipiscing</h3><p>Lorem ipsum dolor sit amet, consectetur adipiscing elit, sed do eiusmod tempor incididunt ut labore et dolore</p><a class="read" href="#">READ MORE</a></div>
</article>
<article class="abs post" style="left:442px;top:2928px">
  <div class="ph" role="img" aria-label="Worker grinding metal with orange sparks in a workshop" style="background:radial-gradient(ellipse 80px 50px at 30% 78%,rgba(255,170,60,.8),transparent 75%),linear-gradient(135deg,#4a4744,#7d746c 50%,#34302d)"></div>
  <div class="box"><div class="date"><svg width="16" height="16" fill="none" stroke="var(--blue)" stroke-width="1.4"><rect x="1" y="3" width="14" height="12"/><path d="M1 7h14M5 1v4M11 1v4"/></svg>November 14, 2021</div><h3>Lorem ipsum doloet, consectetur adipiscing</h3><p>Lorem ipsum dolor sit amet, consectetur adipiscing elit, sed do eiusmod tempor incididunt ut labore et dolore</p><a class="read" href="#">READ MORE</a></div>
</article>
<article class="abs post" style="left:783px;top:2928px">
  <div class="ph" role="img" aria-label="Welder in dark workwear beside a red welding machine" style="background:radial-gradient(ellipse 70px 60px at 22% 35%,rgba(190,50,40,.75),transparent 75%),linear-gradient(135deg,#33363f,#5a5050 50%,#23252e)"></div>
  <div class="box"><div class="date"><svg width="16" height="16" fill="none" stroke="var(--blue)" stroke-width="1.4"><rect x="1" y="3" width="14" height="12"/><path d="M1 7h14M5 1v4M11 1v4"/></svg>November 14, 2021</div><h3>Lorem ipsum doloet, consectetur adipiscing</h3><p>Lorem ipsum dolor sit amet, consectetur adipiscing elit, sed do eiusmod tempor incididunt ut labore et dolore</p><a class="read" href="#">READ MORE</a></div>
</article>

<section class="abs faq">
  <h2 class="abs heading center" style="top:72px;color:#fff">Product FAQ</h2>
  <div class="abs" style="left:109px;top:145px;width:484px">
    <div class="q">The standard Lorem Ipsum passage, used since the 1500s<span class="sign">+</span></div>
    <div class="qa" style="margin-top:13px">
      <div class="q">The standard Lorem Ipsum passage, used since the 1500s<span class="sign">−</span></div>
      <div class="ans"><div role="img" aria-label="Red MIG welding machine" style="flex:0 0 70px;height:90px;background:linear-gradient(180deg,#c0392b,#5a1e18)"></div><div>Lorem ipsum dolor sit amet, consectetur adipiscing elid do eiusmod tempor incididunt ut labore et dolore a ua. Quis ipsum suspendisse ultrices gravida. Risus commodo viverra maecenas accumsan lacus vel facilisis. Lorem ipsum dolor sit amet, consectetur adipiscing elid do eiusmod tempor incididunt ut labore et dolore a ua.</div></div>
    </div>
    <div class="q" style="margin-top:13px">The standard Lorem Ipsum passage, used since the 1500s<span class="sign">+</span></div>
  </div>
  <div class="abs" style="left:606px;top:145px;width:484px;display:flex;flex-direction:column;gap:13px">
    <div class="q">The standard Lorem Ipsum passage, used since the 1500s<span class="sign">+</span></div>
    <div class="q">The standard Lorem Ipsum passage, used since the 1500s<span class="sign">+</span></div>
    <div class="q">The standard Lorem Ipsum passage, used since the 1500s<span class="sign">+</span></div>
    <div class="q">The standard Lorem Ipsum passage, used since the 1500s<span class="sign">+</span></div>
    <div class="q">The standard Lorem Ipsum passage, used since the 1500s<span class="sign">+</span></div>
  </div>
</section>

<div class="news">
  <h2 class="abs heading" style="left:100px;top:4021px">Subscribe to our newsletter</h2>
  <p class="abs" style="left:100px;top:4052px;font-size:13px;color:#333">A short sentence describing what someone will receive by subscribing</p>
  <div class="abs input">Enter Your Email Address</div>
  <a class="abs sub" href="#">SUBSCRIBE</a>
</div>

<div class="abs features">
  <div class="feat a"><svg width="38" height="26" fill="none" stroke="#fff" stroke-width="1.6"><rect x="1" y="4" width="22" height="15"/><path d="M23 9h8l5 5v5H23"/><circle cx="8" cy="21" r="3"/><circle cx="29" cy="21" r="3"/></svg><div><b>Fast Shipping</b>Deliveries throughout Italy</div></div>
  <div class="feat b"><svg width="30" height="30" fill="none" stroke="#fff" stroke-width="1.6"><path d="M4 18v-4a11 11 0 0122 0v4"/><rect x="2" y="17" width="5" height="8" rx="2"/><rect x="23" y="17" width="5" height="8" rx="2"/></svg><div><b>Customer Service</b>From9:00 to 13:00 &nbsp;☏ 02/55510200</div></div>
  <div class="feat a"><svg width="32" height="32" fill="none" stroke="#fff" stroke-width="1.6"><rect x="3" y="3" width="20" height="26"/><path d="M7 10h12M7 15h12M7 20h6"/><circle cx="25" cy="24" r="5"/></svg><div><b>Certified Products</b>Guaranteed, of quality and in<br>accordance with the law</div></div>
  <div class="feat b"><svg width="36" height="28" fill="none" stroke="#fff" stroke-width="1.6"><rect x="1" y="3" width="30" height="20" rx="2"/><path d="M1 9h30M5 17h8"/></svg><div><b>Secure Paymnets</b>Paylink, credit card, Bank Transfer,<br>Cash on Delivery</div></div>
</div>

<footer class="abs footer">
  <div class="abs fcol" style="left:119px;top:55px"><h4>Quick Links</h4><ul><li>Search</li><li>Become a Seller</li><li>Contact Us</li><li>Refund Policy</li><li>Shipping Policy</li><li>Privacy Policy</li><li>Terms of Service</li></ul></div>
  <div class="abs fcol" style="left:310px;top:55px"><h4>Main Menu</h4><ul style="padding-left:4px"><li>Home</li><li>About Us</li><li>Shop</li><li>Blog</li><li>Contact &amp; FAQ</li><li>Press &amp; Awards</li></ul></div>
  <div class="abs fcol" style="left:500px;top:55px;width:340px"><h4>Brazekit</h4>
    <p>do eiusmod tempor incididunt ut labore et dolore magna aliq ua. Ut enim ad minim veniam, quis nostrud exercitation ullam co laboris nisi ut aliquip ex ea commodo consequat. Duis aut e irure dolor in reprehenderit in voluptate velit esse cillum do lore eu fugiat nulla pariatur.</p>
    <p style="margin-top:4px">✉ &nbsp;info@brazekit.com</p>
    <p style="margin-top:4px">☏ &nbsp;+31(0)645217390</p>
  </div>
  <div class="abs fcol" style="left:881px;top:55px;width:260px"><h4>News &amp; Updates</h4>
    <p style="line-height:29px">Sign up to get the latest on<br>sales, new releases and more ...</p>
    <div class="femail" style="margin-top:10px">Enter your email<svg width="30" height="30"><circle cx="15" cy="15" r="15" fill="var(--yellow)"/><path d="M8 15l14-6-5 14-2-6z" fill="#fff"/></svg></div>
    <div class="social" style="margin-top:20px"><i></i><i></i><i></i><i></i></div>
  </div>
  <div class="abs" style="left:119px;top:342px;font-size:13px">Copyright © 2021 brazekit All Rights Reserved.</div>
  <div class="abs pay" style="left:795px;top:340px"><span>Cardly</span><span>Mondo</span><span>Amberpay</span><span>Paylink</span><span>Tapwise</span></div>
</footer>

</body>
</html>
```